Bref créative
Business Card Design for Law Firm
Harlow Legal Partners
Professional
Derek M. Falbo
Trial Lawyer
2730 Birchwood Avenue
North Annex - Suite 2100
Philadelphia, PA 19102
555-014-2737 (use as place holder)
derek@harlowcounsel.example
www.harlowcounsel.example
I am looking for a bold logo and business card design for a start-up law firm based in Philadelphia and with offices in PA and NJ. Harlow Legal Partners is led by trial attorneys and specializes in catastrophic personal injury litigation stemming from construction / industrial accidents, truck/auto accidents, defective products, falls, and medical malpractice.
New #s for phone and fax will be supplied upon selection of winning design.
Areas of Expertise:
- Personal Injury
- Wrongful Death
- Construction Accidents
- Work Injuries
- Car & Truck Accidents
- Motorcycle Accidents
- Medical Malpractice
- Nursing Home Abuse
- Premises Liability
- Longshore / Maritime
- Commercial Litigation
White Version
Black Version

```html
<!DOCTYPE html>
<html lang="en">
<head>
<meta charset="utf-8">
<title>Harlow Legal Partners – Stationery Set</title>
<link href="https://fonts.googleapis.com/css2?family=Montserrat:wght@400;600;700&display=swap" rel="stylesheet">
<style>
  :root{
    --stage:#5d5f63;
    --paper:#ffffff;
    --blue:#1f74c9;
    --blue-deep:#0f4f9a;
    --blue-light:#8ec3f0;
    --ink:#2b3440;
    --muted:#8a939d;
  }
  html,body{margin:0;padding:0;overflow:hidden}
  body{width:1200px;height:247px;background:var(--stage);font-family:"Montserrat",sans-serif;position:relative;color:var(--ink)}
  .piece{position:absolute;background:var(--paper);overflow:hidden;box-shadow:0 1px 3px rgba(0,0,0,.45)}
  .piece svg.swoosh{position:absolute;left:0;width:100%;display:block}
  .brand{position:absolute;display:flex;align-items:center;gap:2px;font-weight:700;color:var(--blue);white-space:nowrap;line-height:1}
  .brand .dot{border-radius:50%;background:var(--blue);flex:none}
  .tiny{position:absolute;font-size:3px;line-height:4.2px;color:var(--muted);white-space:nowrap}
  .on-blue{color:#fff}
  .on-blue .dot{background:#fff}
  .blue-fill{background:linear-gradient(135deg,var(--blue) 0%,var(--blue-deep) 100%)}
</style>
</head>
<body>

<!-- Business cards -->
<div class="piece blue-fill card" style="left:10px;top:18px;width:98px;height:56px">
  <div class="brand on-blue" style="left:7px;top:24px;font-size:5.6px;gap:3px"><span class="dot" style="width:7px;height:7px"></span>Harlow Legal Partners</div>
</div>

<div class="piece card" style="left:10px;top:100px;width:47px;height:28px">
  <svg class="swoosh" style="bottom:0;height:9px" viewBox="0 0 47 9" preserveAspectRatio="none"><path d="M0 4 Q24 0 47 3 V9 H0Z" fill="var(--blue)"/></svg>
  <div class="brand" style="left:3px;top:4px;font-size:2.6px"><span class="dot" style="width:3px;height:3px"></span>Harlow Legal Partners</div>
  <div class="tiny" style="left:4px;top:10px;font-size:2.3px;line-height:3px">Derek M. Falbo<br>555-014-2737</div>
</div>
<div class="piece blue-fill card" style="left:61px;top:100px;width:47px;height:28px">
  <div class="brand on-blue" style="left:4px;top:12px;font-size:2.6px"><span class="dot" style="width:3px;height:3px"></span>Harlow Legal Partners</div>
</div>
<div class="piece card" style="left:10px;top:190px;width:47px;height:28px">
  <svg class="swoosh" style="top:0;height:8px" viewBox="0 0 47 8" preserveAspectRatio="none"><path d="M0 0 H47 V5 Q24 8 0 4Z" fill="var(--blue)"/></svg>
  <div class="tiny" style="left:3px;top:11px;font-size:2.3px;line-height:3px">2730 Birchwood Avenue<br>North Annex - Suite 2100<br>derek@harlowcounsel.example</div>
</div>
<div class="piece card" style="left:61px;top:190px;width:47px;height:28px">
  <div class="brand" style="left:4px;top:12px;font-size:2.6px"><span class="dot" style="width:3px;height:3px"></span>Harlow Legal Partners</div>
</div>

<!-- Letterhead 1 -->
<div class="piece letterhead" style="left:118px;top:12px;width:107px;height:225px">
  <svg class="swoosh" style="top:0;height:40px" viewBox="0 0 107 40" preserveAspectRatio="none">
    <path d="M0 0 H107 V22 Q55 40 0 18Z" fill="var(--blue)"/>
    <path d="M0 22 Q55 44 107 26" stroke="var(--blue-light)" stroke-width="1" fill="none"/>
  </svg>
  <div class="brand on-blue" style="left:40px;top:7px;font-size:4px"><span class="dot" style="width:5px;height:5px"></span>Harlow Legal Partners</div>
  <div class="tiny" style="left:8px;top:52px">Dear Mr. Reed,</div>
  <div class="tiny" style="left:8px;top:60px">We appreciate your trust in our firm and<br>look forward to working with you.</div>
  <div class="tiny" style="left:8px;top:178px">Sincerely,</div>
  <svg class="swoosh" style="bottom:0;height:14px" viewBox="0 0 107 14" preserveAspectRatio="none"><path d="M0 8 Q55 0 107 6 V14 H0Z" fill="var(--blue)"/></svg>
  <div class="tiny on-blue" style="left:14px;bottom:2px;font-size:2.4px">www.harlowcounsel.example · 555-014-2737</div>
</div>

<!-- Letterhead 2 -->
<div class="piece letterhead" style="left:232px;top:12px;width:107px;height:225px">
  <svg class="swoosh" style="top:0;height:34px" viewBox="0 0 107 34" preserveAspectRatio="none">
    <path d="M0 0 H107 V14 Q50 34 0 20Z" fill="var(--blue)"/>
  </svg>
  <div class="brand on-blue" style="left:6px;top:6px;font-size:4px"><span class="dot" style="width:5px;height:5px"></span>Harlow Legal Partners</div>
  <div class="tiny" style="left:8px;top:48px">Dear Mr. Reed,</div>
  <div class="tiny" style="left:8px;top:56px">We appreciate your trust in our firm and<br>look forward to working with you.</div>
  <div class="tiny" style="left:8px;top:178px">Sincerely,</div>
  <svg class="swoosh" style="bottom:0;height:12px" viewBox="0 0 107 12" preserveAspectRatio="none"><path d="M0 6 Q55 0 107 5 V12 H0Z" fill="var(--blue)"/></svg>
</div>

<!-- Compliment card -->
<div class="piece blue-fill compliment" style="left:346px;top:95px;width:80px;height:42px">
  <div class="brand on-blue" style="left:7px;top:18px;font-size:4.4px"><span class="dot" style="width:5px;height:5px"></span>Harlow Legal Partners</div>
</div>
<div class="piece note" style="left:432px;top:95px;width:40px;height:26px">
  <svg class="swoosh" style="bottom:0;height:8px" viewBox="0 0 40 8" preserveAspectRatio="none"><path d="M0 4 Q20 0 40 3 V8 H0Z" fill="var(--blue)"/></svg>
  <div class="brand" style="left:3px;top:6px;font-size:2.2px;gap:1.5px"><span class="dot" style="width:2.5px;height:2.5px"></span>Harlow Legal Partners</div>
</div>

<!-- Envelopes -->
<div class="piece envelope" style="left:482px;top:82px;width:98px;height:36px">
  <svg class="swoosh" style="bottom:0;height:11px" viewBox="0 0 98 11" preserveAspectRatio="none"><path d="M0 5 Q50 0 98 4 V11 H0Z" fill="var(--blue)"/></svg>
  <div class="brand" style="left:5px;top:5px;font-size:3.2px"><span class="dot" style="width:4px;height:4px"></span>Harlow Legal Partners</div>
  <div class="tiny" style="left:5px;top:11px;font-size:2.3px;line-height:3px">2730 Birchwood Avenue<br>North Annex - Suite 2100</div>
</div>
<div class="piece envelope" style="left:482px;top:124px;width:98px;height:36px">
  <svg class="swoosh" style="top:0;height:18px" viewBox="0 0 98 18" preserveAspectRatio="none"><path d="M0 0 H98 V4 L49 18 L0 4Z" fill="#e6ebf0"/></svg>
  <svg class="swoosh" style="bottom:0;height:8px" viewBox="0 0 98 8" preserveAspectRatio="none"><path d="M0 4 Q50 0 98 3 V8 H0Z" fill="var(--blue)"/></svg>
</div>
<div class="piece envelope" style="left:592px;top:82px;width:110px;height:36px">
  <svg class="swoosh" style="top:0;height:12px" viewBox="0 0 110 12" preserveAspectRatio="none"><path d="M0 0 H110 V5 Q55 12 0 6Z" fill="var(--blue)"/></svg>
  <div class="brand" style="left:6px;top:18px;font-size:3.2px"><span class="dot" style="width:4px;height:4px"></span>Harlow Legal Partners</div>
</div>
<div class="piece blue-fill envelope" style="left:592px;top:124px;width:110px;height:36px">
  <svg class="swoosh" style="top:0;height:16px" viewBox="0 0 110 16" preserveAspectRatio="none"><path d="M0 0 H110 L55 16Z" fill="var(--blue-deep)"/></svg>
</div>

<!-- Folder -->
<div class="piece folder" style="left:866px;top:10px;width:164px;height:225px">
  <svg class="swoosh" style="top:60px;height:60px" viewBox="0 0 164 60" preserveAspectRatio="none">
    <path d="M0 20 Q80 0 164 14 V42 Q80 30 0 52Z" fill="var(--blue)"/>
  </svg>
  <div class="piece" style="left:8px;top:150px;width:148px;height:60px;box-shadow:none;background:#f1f4f7"></div>
  <div class="piece card" style="left:110px;top:170px;width:36px;height:20px;box-shadow:0 0 2px rgba(0,0,0,.3)">
    <div class="brand" style="left:3px;top:8px;font-size:2px;gap:1.5px"><span class="dot" style="width:2.5px;height:2.5px"></span>Harlow Legal Partners</div>
  </div>
</div>
<div class="piece folder" style="left:1031px;top:10px;width:164px;height:225px">
  <svg class="swoosh" style="top:0;height:225px" viewBox="0 0 164 225" preserveAspectRatio="none">
    <path d="M164 0 V225 H90 Q150 120 120 0Z" fill="var(--blue)"/>
    <path d="M110 0 Q140 120 80 225" stroke="var(--blue-light)" stroke-width="1.2" fill="none"/>
  </svg>
  <div class="brand" style="left:14px;top:55px;font-size:6px;gap:3px"><span class="dot" style="width:9px;height:9px"></span>Harlow Legal Partners</div>
</div>

</body>
</html>
```